Brix2Key Header

I want a professional Letterhead for my law firm. I'm attaching the letterhead I currently use in Word and PDF form. I'm also attaching my logo, and an example header that I like.

```html
<!DOCTYPE html>
<html lang="en">
<head>
<meta charset="utf-8">
<title>Brix2Key Letterhead</title>
<link href="https://fonts.googleapis.com/css2?family=Noto+Sans:ital,wght@0,400;0,700;0,800;1,400&family=Tinos&display=swap" rel="stylesheet">
<style>
  :root {
    --brand-blue: #1aa9dc;
    --ink: #222222;
    --ink-soft: #333333;
    --rule: #9fd6ea;
    --paper: #ffffff;
    --backdrop: #e9e9e9;
  }
  * { box-sizing: border-box; margin: 0; padding: 0; }
  html, body { width: 1100px; height: 1200px; overflow: hidden; background: var(--backdrop); }
  body { font-family: "Noto Sans", Verdana, sans-serif; color: var(--ink); }
  .page { position: absolute; left: 126px; top: 0; width: 848px; height: 1200px; background: var(--paper); }
  .abs { position: absolute; }
  .firm-name { left: 57px; top: 62px; font-family: "Tinos", serif; font-size: 18px; color: var(--brand-blue); white-space: nowrap; }
  .firm-name small { font-family: "Noto Sans", sans-serif; font-size: 12px; color: var(--ink); margin-left: 6px; }
  .header-rule { left: 57px; top: 180px; width: 729px; height: 1px; background: var(--rule); }
  .contact { font-size: 12.5px; color: var(--ink-soft); display: flex; align-items: center; gap: 9px; white-space: nowrap; }
  .contact svg { width: 11px; height: 11px; fill: var(--brand-blue); flex: none; }
  .brand-name { left: 524px; top: 70px; width: 262px; text-align: right; font-size: 50px; font-weight: 800; color: #111; letter-spacing: -1px; line-height: 1; }
  .strong { font-weight: 700; }
  .line-fax { left: 57px; top: 254px; font-size: 13px; font-weight: 700; letter-spacing: .3px; }
  .line-date { right: 62px; top: 254px; font-size: 13px; font-weight: 700; letter-spacing: .3px; word-spacing: 8px; }
  .recipient { left: 57px; top: 314px; font-size: 13.5px; line-height: 20px; }
  .subject { left: 0; width: 848px; top: 435px; text-align: center; font-size: 13.5px; font-weight: 700; letter-spacing: .3px; }
  .claim { left: 0; width: 848px; top: 455px; text-align: center; font-size: 13.5px; }
  .claim .sep { margin: 0 8px; }
  .salutation { left: 57px; top: 516px; font-size: 13.5px; font-weight: 700; }
  .body-copy { left: 57px; top: 555px; width: 728px; font-size: 13.6px; letter-spacing: .25px; line-height: 20.3px; text-align: justify; color: var(--ink-soft); }
  .body-copy p + p { margin-top: 20.3px; }
  .closing { left: 57px; top: 859px; font-size: 13.5px; }
  .signature { left: 57px; top: 880px; width: 165px; height: 62px; background: linear-gradient(90deg, rgba(26,169,220,.18), rgba(26,169,220,.06)); }
  .signer { left: 57px; top: 960px; font-size: 13.5px; line-height: 20px; }
  .signer em { font-style: italic; }
  .footer-band { left: 0; top: 1160px; width: 848px; height: 6px; background: var(--brand-blue); }
</style>
</head>
<body>
<main class="page">
  <div class="abs firm-name">Bernard K. Ramirez IV<small>Attorney at Law, PLLC</small></div>

  <div class="abs contact" style="left:57px;top:104px">
    <svg viewBox="0 0 12 12"><path d="M0 2h12v8H0z M0 2l6 5 6-5" stroke="#fff" stroke-width=".8"/></svg>bk@brix2key.com
  </div>
  <div class="abs contact" style="left:57px;top:122px">
    <svg viewBox="0 0 12 12"><circle cx="6" cy="6" r="5.5"/><path d="M.5 6h11M6 .5v11" stroke="#fff" stroke-width=".8"/></svg>www.brix2key.com
  </div>
  <div class="abs contact" style="left:205px;top:104px">
    <svg viewBox="0 0 12 12"><circle cx="6" cy="6" r="6"/><path d="M4 3l1 2-1 1 2 2 1-1 2 1-1 2C5 10 2 7 2 4z" fill="#fff"/></svg>(877) 555-0142
  </div>
  <div class="abs contact" style="left:205px;top:122px">
    <svg viewBox="0 0 12 12"><path d="M0 4c2-3 10-3 12 0v2H9V4H3v2H0z M2 7h8l1 4H1z"/></svg>(469) 555-0187
  </div>
  <div class="abs contact" style="left:57px;top:146px">
    <svg viewBox="0 0 12 12"><path d="M6 0a4.5 4.5 0 0 1 4.5 4.5C10.5 8 6 12 6 12S1.5 8 1.5 4.5A4.5 4.5 0 0 1 6 0z"/><circle cx="6" cy="4.5" r="1.7" fill="#fff"/></svg>2240 Harwood St. Ste 300 Dallas, TEXAS 75201
  </div>

  <div class="abs brand-name">Brix2Key</div>
  <div class="abs header-rule"></div>

  <div class="abs line-fax">VIA FACSIMILE : (800)-555-0163</div>
  <div class="abs line-date">July 11, 2021</div>

  <div class="abs recipient">
    <div><span class="strong">Attn:</span> Daniel Hayes</div>
    <div class="strong">Lonestar Mutual Insurance</div>
    <div>4820 Preston Road 210 Dallas, Texas 75240</div>
    <div>Tel: (972)-555-0110</div>
  </div>

  <div class="abs subject">RE : NOTICE OF &nbsp;REPRESENTATION</div>
  <div class="abs claim">Claim Number: <span class="strong">2048316-TX</span><span class="sep">|</span>Date of Accident: <span class="strong">February 3, 2018</span><span class="sep">|</span>My client: <span class="strong">John Doe</span></div>

  <div class="abs salutation">Dear Mr. Daniel Hayes,</div>

  <div class="abs body-copy">
    <p>Lorem Ipsum is simply dummy text of the printing and typesetting industry. Lorem Ipsum has been the industry's standard dummy text ever since the 1500s, when an unknown printer took a galley of type and scrambled it to make a type specimen book. It has survived not only five centuries, but also the leap into electronic typesetting, remaining essentially unchanged. It was popularised in the 1960s with the release of transfer sheets containing Lorem Ipsum passages, and more recently with desktop publishing and page layout tools including versions of Lorem Ipsum.</p>
    <p>Lorem Ipsum is simply dummy text of the printing and typesetting industry. Lorem Ipsum has been the industry's standard dummy text ever since the 1500s, when an unknown printer took a galley of type and scrambled it to make a type specimen book. It has survived not only five centuries, but also the leap into electronic typesetting, remaining essentially unchanged. I</p>
  </div>

  <div class="abs closing">Sincerely,</div>
  <div class="abs signature" role="img" aria-label="Handwritten signature of the attorney"></div>
  <div class="abs signer">
    <div class="strong">Bernard K. Ramirez</div>
    <div><em>Attorney at Law</em></div>
  </div>

  <div class="abs footer-band"></div>
</main>
</body>
</html>
```